INNOVATION WEBSITE NEEDED: Agency from NZ needs YOU

Please see the enclosed documents for a detailed brief. It needs to be clean / simple / elegant / premium looking - that will appeal to companies that range from start-up to multi-national!
Note:
Perhaps instead of an actual shop, people can press an 'enquire now' button?

Target Market(s)

Start ups to multi-nationals

Industry/Entity Type

Marketing

Number of Pages Required

5+ page

Requirements
Must have
• Wordpress
• SEO
• Format friendly (mobile / tablet / etc)
• I have the URL: www.dr-lanternfix.com - I would like a working website. Please let me know what else you require to 'go live' with. Thanks!
Nice to have
• Please use / improve on my current ideas
• Perhaps use my logo icon (in different colours) for each 'product'?

```html
<!DOCTYPE html>
<html lang="en">
<head>
<meta charset="utf-8">
<title>Dr-Lanternfix — Creating the Future</title>
<link rel="stylesheet" href="https://fonts.googleapis.com/css2?family=Michroma&family=Roboto:wght@400;500;700&display=swap">
<style>
:root{
  --navy:#2c2a6b;
  --navy-deep:#24225c;
  --sky:#29a8e0;
  --sky-light:#35b3ea;
  --grey-card:#efefef;
  --ink:#2b2b2b;
  --white:#ffffff;
}
*{margin:0;padding:0;box-sizing:border-box}
html,body{width:1200px;height:2462px;overflow:hidden}
body{position:relative;background:var(--white);font-family:'Roboto',Arial,sans-serif;color:var(--ink)}
.abs{position:absolute}
.display{font-family:'Michroma','Roboto',sans-serif}

/* utility bar */
.utility-bar{left:419px;top:0;width:533px;height:18px;background:var(--navy-deep);clip-path:polygon(14px 0,100% 0,100% 100%,0 100%);display:flex;align-items:center;padding-left:24px;font-size:8.5px;color:#fff;font-weight:500}
.utility-bar a{color:#fff;text-decoration:none}
.utility-bar .sep{margin:0 11px;opacity:.8}
.utility-bar .social{margin-left:auto;display:flex;gap:5px;padding-right:10px}
.utility-bar .social span{width:8px;height:8px;border-radius:50%;background:#fff;display:block}

/* header */
.brand{left:263px;top:38px;display:flex;align-items:center;gap:8px}
.brand-dot{width:26px;height:26px;border-radius:50%;background:var(--navy)}
.brand-name{font-size:19px;font-weight:700;color:var(--navy);letter-spacing:.5px}
.main-nav{left:566px;top:56px;display:flex;gap:17px;font-size:11.5px;font-weight:500;color:var(--navy)}
.main-nav a{color:var(--navy);text-decoration:none;padding-bottom:6px}
.main-nav a.active{color:var(--sky);border-bottom:2px solid var(--sky)}

/* hero */
.hero-photo{left:0;top:100px;width:1200px;height:409px;background:linear-gradient(100deg,#d9d5cf 0%,#bfb9b1 25%,#8f96a8 45%,#cfcbc4 62%,#e2ddd6 100%)}
.hero-title{left:591px;top:182px;font-size:21px;font-weight:700;color:var(--navy);letter-spacing:.5px}
.hero-sub{left:612px;top:216px;width:330px;font-size:11.5px;line-height:14px;text-align:center;color:#222}
.btn-solid{background:var(--sky);color:#fff;font-size:11px;font-weight:500;display:flex;align-items:center;justify-content:center;text-decoration:none}
.hero-cta{left:712px;top:259px;width:105px;height:30px}
.hero-dots{left:591px;top:493px;display:flex;gap:4px}
.hero-dots span{width:6px;height:6px;border-radius:50%;background:var(--sky)}

/* section headings */
.section-title{left:0;width:1200px;text-align:center;font-size:19px;color:var(--navy)}
.divider{height:1px;background:var(--navy)}
.divider::after{content:"";position:absolute;left:50%;top:-5px;width:10px;height:10px;margin-left:-5px;border:1.5px solid var(--navy);border-radius:50%;background:#fff}

/* service cards */
.service-card{top:579px;width:217px;height:355px;background:var(--grey-card)}
.service-card .cap{height:171px;background:var(--sky);position:relative}
.icon-disc{position:absolute;left:50%;top:16px;width:138px;height:138px;margin-left:-69px;border-radius:50%;background:var(--navy);border:5px solid #fff;display:flex;align-items:center;justify-content:center}
.service-card h3{margin-top:46px;text-align:center;font-size:17.5px;font-weight:500;color:var(--navy)}
.service-card .price{text-align:center;font-size:17.5px;color:var(--navy);margin-top:2px}
.btn-outline{display:flex;margin:17px auto 0;width:105px;height:28px;border:1px solid var(--sky);color:var(--sky);font-size:10.5px;align-items:center;justify-content:center;text-decoration:none;background:#fff}

/* kick-start band */
.kickstart{left:0;top:954px;width:1200px;height:269px;background:linear-gradient(90deg,var(--navy-deep),#36347a 50%,var(--navy-deep))}
.kickstart-inner{position:absolute;left:256px;top:20px;width:620px;color:#fff;font-size:12.5px;line-height:18.5px}
.kickstart h2{font-family:'Michroma','Roboto',sans-serif;color:var(--sky-light);font-size:14px;font-weight:400;margin-bottom:12px}
.kickstart .lead-q{color:var(--sky-light);margin:12px 0 6px}
.tick-list{list-style:none}
.tick-list li{display:flex;align-items:center;gap:9px}
.tick-list svg{flex:none}
.kickstart .closing{margin-top:10px}

/* info cards */
.info-card{top:1243px;width:217px;height:410px;border:1px solid var(--navy);background:#fff}
.info-card .cap{height:170px;background:var(--sky);position:relative}
.info-card .cap .icon-disc{top:14px}
.info-card h3{font-family:'Michroma','Roboto',sans-serif;font-weight:400;font-size:15px;color:var(--navy);margin:12px 0 0 8px}
.info-card .body{margin:12px 10px 0 10px;font-size:8.3px;line-height:11px;color:#333}
.info-card .body p{margin-bottom:9px}

/* newsletter */
.newsletter{left:0;top:1671px;width:1200px;height:204px;background:linear-gradient(180deg,#e6e8ef,#d7dae6 60%,#e3e5ec)}
.newsletter .section-title{top:36px}
.newsletter .note{position:absolute;left:0;width:1200px;top:72px;text-align:center;font-size:9.5px;line-height:13px;font-weight:700;color:#222}
.mail-field{left:369px;top:123px;width:343px;height:40px;background:var(--navy);color:#fff;font-size:12px;font-style:italic;display:flex;align-items:center;padding-left:14px}
.mail-submit{left:729px;top:123px;width:103px;height:40px;background:var(--navy);color:#fff;font-size:12px;font-weight:500;display:flex;align-items:center;justify-content:center}

/* contact */
.contact{left:0;top:1894px;width:1200px;height:526px;background:linear-gradient(180deg,#333181,#2d2b77 50%,#34328a)}
.contact .section-title{color:#fff;top:18px}
.contact .divider{background:#8fb6e6}
.contact .divider::after{background:#2f2d7c;border-color:var(--sky)}
.contact .note{position:absolute;left:0;width:1200px;top:74px;text-align:center;font-size:9.5px;line-height:13px;font-weight:700;color:#fff}
.contact-point{position:absolute;top:137px;width:300px;text-align:center;color:#fff}
.contact-point .bubble{width:43px;height:43px;border-radius:50%;background:var(--sky);margin:0 auto;display:flex;align-items:center;justify-content:center}
.contact-point h4{margin-top:14px;font-size:11px;font-weight:700}
.contact-point p{margin-top:8px;font-size:11.5px;line-height:14px}
.field{position:absolute;border:1px solid var(--sky);color:#fff;font-size:10px;padding:10px 12px}
.send{left:529px;top:468px;width:110px;height:36px;font-size:12px}

/* footer */
.site-footer{left:0;top:2420px;width:1200px;height:42px;background:var(--sky);color:#fff;font-size:9px;display:flex;align-items:center;padding-left:249px}
.site-footer b{font-weight:700;margin:0 3px}
</style>
</head>
<body>

<nav class="utility-bar abs">
  <a href="#">My Account</a><span class="sep">|</span>
  <a href="#">Register</a><span class="sep">|</span>
  <a href="#">Terms And Conditions</a><span class="sep">|</span>
  <a href="#">FAQ</a><span class="sep">|</span>
  <a href="#">Support</a>
  <div class="social"><span></span><span></span><span></span><span></span></div>
</nav>

<div class="brand abs"><span class="brand-dot"></span><span class="brand-name">Dr-Lanternfix</span></div>

<nav class="main-nav abs">
  <a class="active" href="#">HOME</a><a href="#">SHOP</a><a href="#">OUR PURPOSE</a><a href="#">WHAT WE DO</a><a href="#">OUR TEAM</a><a href="#">CONTACT US</a>
</nav>

<section>
  <div class="hero-photo abs" role="img" aria-label="Photo of a thoughtful businessman at a laptop in a bright office"></div>
  <h1 class="hero-title abs display">WELCOME TO DR-LANTERNFIX</h1>
  <p class="hero-sub abs">Finding it hard to get all the different functions aligned and there-fore getting no where on innovation?"</p>
  <a class="hero-cta btn-solid abs" href="#">BUY NOW</a>
  <div class="hero-dots abs"><span></span><span></span><span></span><span></span></div>
</section>

<h2 class="section-title display abs" style="top:527px">OUR SERVICES</h2>
<div class="divider abs" style="left:425px;top:560px;width:343px"></div>

<article class="service-card abs" style="left:266px">
  <div class="cap"><div class="icon-disc">
    <svg width="70" height="60" viewBox="0 0 70 60" fill="#29a8e0"><rect x="4" y="40" width="10" height="18"/><rect x="19" y="32" width="10" height="26"/><rect x="34" y="36" width="10" height="22"/><rect x="49" y="24" width="10" height="34"/><path d="M4 30 L22 16 L36 24 L58 6" stroke="#29a8e0" stroke-width="5" fill="none"/><path d="M50 2 L64 2 L64 16 Z"/></svg>
  </div></div>
  <h3>THE BARISTA</h3><div class="price">$FREE</div>
  <a class="btn-outline" href="#">BUY NOW</a>
</article>
<article class="service-card abs" style="left:491px">
  <div class="cap"><div class="icon-disc">
    <svg width="70" height="70" viewBox="0 0 70 70" fill="none" stroke="#29a8e0" stroke-width="4"><path d="M35 4 v26 M42 10 h-10 a5 5 0 0 0 0 10 h6 a5 5 0 0 1 0 10 h-10"/><path d="M6 44 L34 36 L64 44 L36 52 Z M6 52 L36 60 L64 52 M6 60 L36 68 L64 60"/></svg>
  </div></div>
  <h3>THE JEDI KNIGHT</h3><div class="price">$499</div>
  <a class="btn-outline" href="#">BUY NOW</a>
</article>
<article class="service-card abs" style="left:716px">
  <div class="cap"><div class="icon-disc">
    <svg width="76" height="76" viewBox="0 0 76 76"><g stroke="#29a8e0" stroke-width="3"><path d="M38 2v8M12 12l6 6M64 12l-6 6M2 36h8M66 36h8"/></g><circle cx="38" cy="36" r="20" fill="#29a8e0"/><rect x="28" y="54" width="20" height="14" rx="3" fill="#29a8e0"/><rect x="35.5" y="24" width="5" height="15" fill="#2c2a6b"/><circle cx="38" cy="45" r="3" fill="#2c2a6b"/></svg>
  </div></div>
  <h3>THE NINJA</h3><div class="price">$749</div>
  <a class="btn-outline" href="#">BUY NOW</a>
</article>

<section class="kickstart abs" role="img" aria-label="Faint background photo of business charts on navy">
  <div class="kickstart-inner">
    <h2>RE-BOOT OR KICK-START...?</h2>
    <p>Do you need to reboot or kick-start your company's innovation capabilities in terms of process, people or proj-ects?</p>
    <p class="lead-q">Do you need:</p>
    <ul class="tick-list">
      <li><svg width="12" height="12" viewBox="0 0 12 12"><rect x="1" y="1" width="10" height="10" fill="none" stroke="#fff" stroke-width="1.3"/><path d="M3 6l2 2 6-7" stroke="#fff" stroke-width="1.8" fill="none"/></svg>a new way of doing something?</li>
      <li><svg width="12" height="12" viewBox="0 0 12 12"><rect x="1" y="1" width="10" height="10" fill="none" stroke="#fff" stroke-width="1.3"/><path d="M3 6l2 2 6-7" stroke="#fff" stroke-width="1.8" fill="none"/></svg>a brilliant breakthrough idea?</li>
      <li><svg width="12" height="12" viewBox="0 0 12 12"><rect x="1" y="1" width="10" height="10" fill="none" stroke="#fff" stroke-width="1.3"/><path d="M3 6l2 2 6-7" stroke="#fff" stroke-width="1.8" fill="none"/></svg>a 3-5 year roadmap of strategic innovation?</li>
    </ul>
    <p class="closing">Or simply a new perspective to jump start the team?<br>If you have answered yes to any of the above, contact Dr-Lanternfix!<br>We create innovation that hits the bottom line.</p>
  </div>
</section>

<article class="info-card abs" style="left:266px">
  <div class="cap"><div class="icon-disc">
    <svg width="74" height="74" viewBox="0 0 74 74" fill="#29a8e0"><path d="M8 22h16a7 7 0 1 1 14 0h16v16a7 7 0 1 1 0 14v16H38a7 7 0 1 0-14 0H8V52a7 7 0 1 0 0-14z"/></svg>
  </div></div>
  <h3>OUR PURPOSE</h3>
  <div class="body">
    <p>Our purpose is to re-define how companies like yours get great innovation. Quickly.</p>
    <p>The team at Dr-Lanternfix have worked both client side and as consultants. We know what works and how things tick internally. It's not just about pretty pictures. Ideas need to stack up: strategically, culturally and commercially.</p>
    <p>We get that. We can help you achieve that.<br>That's our purpose.</p>
  </div>
</article>
<article class="info-card abs" style="left:491px">
  <div class="cap"><div class="icon-disc">
    <svg width="72" height="72" viewBox="0 0 72 72" fill="#29a8e0"><circle cx="36" cy="36" r="16"/><g stroke="#29a8e0" stroke-width="8"><path d="M36 12v48M12 36h48M19 19l34 34M53 19L19 53"/></g><circle cx="36" cy="36" r="7" fill="#2c2a6b"/></svg>
  </div></div>
  <h3>WHAT WE DO</h3>
  <div class="body">
    <p>We innovate. For you</p>
    <p><b>The most common things we hear are:</b></p>
    <p>"I need a breakthrough innovation, but am staring at a blank piece of paper"<br>"I have to come up with a great idea, but have a limited budget and little time"<br>"It's hard to get all the different functions and</p>
    <p>That's where we can help. We've been there and done that...many times. What we do is:</p>
    <p>Deliver big ideas!<br>Fast and affordable<br>Get buy-in at all levels.</p>
  </div>
</article>
<article class="info-card abs" style="left:716px">
  <div class="cap"><div class="icon-disc">
    <svg width="76" height="72" viewBox="0 0 76 72" fill="#29a8e0"><circle cx="46" cy="26" r="15"/><g stroke="#29a8e0" stroke-width="6"><path d="M46 4v44M24 26h44M31 11l30 30M61 11L31 41"/></g><circle cx="46" cy="26" r="6" fill="#2c2a6b"/><circle cx="20" cy="52" r="10"/><g stroke="#29a8e0" stroke-width="5"><path d="M20 36v32M4 52h32M9 41l22 22M31 41L9 63"/></g><circle cx="20" cy="52" r="4" fill="#2c2a6b"/></svg>
  </div></div>
  <h3>HOW IT WORKS</h3>
  <div class="body">
    <p>Instead of asking for a quote like with most agencies, we have a price list. You can order our services online!</p>
    <p>There's no back and forwards with long winded quotes that have taken your briefing, reworded it and sent it back to you with a huge price tag attached!</p>
    <p>Simply have a look at our innovation shop window and if you like what you see and know exactly what you want, you push the 'Buy' button. And then we will start working.</p>
    <p>If you want to talk beforehand, simply give the team at Dr-Lanternfix a call and we can have a quick chat first.</p>
  </div>
</article>

<section class="newsletter abs" role="img" aria-label="Soft background photo of financial data in pale blue">
  <h2 class="section-title display abs">SUBSCRIBE TO OUR NEWSLETTER</h2>
  <p class="note">Lorem Ipsum is simply dummy text of the printing and typesetting industry.<br>Lorem Ipsum has been the industry's standard dummy text ever since the 1500s</p>
  <div class="mail-field abs">Your Mail</div>
  <div class="mail-submit abs">Subscribe</div>
</section>

<section class="contact abs">
  <h2 class="section-title display abs">CONTACT US</h2>
  <div class="divider abs" style="left:425px;top:56px;width:343px"></div>
  <p class="note">Lorem Ipsum is simply dummy text of the printing and typesetting industry.<br>Lorem Ipsum has been the industry's standard dummy text ever since the 1500s</p>

  <div class="contact-point" style="left:210px">
    <div class="bubble"><svg width="18" height="16" viewBox="0 0 18 16" fill="#2c2a6b"><path d="M9 0L0 8h3v8h4v-5h4v5h4V8h3z"/></svg></div>
    <h4>ADDRESS</h4><p>12 Harbour Lane, Kelp Bay,<br>Tui Island, Auckland, New Zealand</p>
  </div>
  <div class="contact-point" style="left:451px">
    <div class="bubble"><svg width="18" height="16" viewBox="0 0 18 16" fill="#2c2a6b"><path d="M9 0C4 0 0 3 0 7c0 2 1 4 3 5l-1 4 4-3c1 .2 2 .3 3 .3 5 0 9-3 9-6.6S14 0 9 0z"/></svg></div>
    <h4>MAIL</h4><p>hello@dr-lanternfix.com (tbc)</p>
  </div>
  <div class="contact-point" style="left:690px">
    <div class="bubble"><svg width="16" height="16" viewBox="0 0 16 16" fill="#2c2a6b"><path d="M3 0l3 4-2 2c1 2 4 5 6 6l2-2 4 3-2 3C7 16 0 9 0 3z"/></svg></div>
    <h4>PHONE</h4><p>64 21 0000 555</p>
  </div>

  <div class="field" style="left:250px;top:265px;width:221px;height:39px">Enter Name</div>
  <div class="field" style="left:491px;top:265px;width:221px;height:39px">Enter Mail</div>
  <div class="field" style="left:731px;top:265px;width:220px;height:39px">Enter Subject</div>
  <div class="field" style="left:250px;top:324px;width:701px;height:125px">Enter Message</div>
  <a class="send btn-solid abs" href="#">Send Message</a>
</section>

<footer class="site-footer abs">© Copyright 2016 <b>Dr-Lanternfix</b> All Rights Reserved.</footer>

</body>
</html>
```